Word Cloud Graphic Wallpaper design

The following sentences need to be put together in an ai file of the size : 70" wide and 108" high . This will be used as a wall paper. Inspirational image is attached. (We have also attached a rough idea showing you the wall it would go one- DO NOT REPLICATE THE LAYOUT OF THE SENTENCES-This only shows you how we will be using your file)

Sentences are:

Dentistry is not Expensive Neglect is!
Smiles are free but they are worth alot.
Don't Forget to Floss!
Put on your best SMILE everyday!
Be the reason someone smiles today.
Let your SMILE CHANGE THE WORLD, don't let the world change your smile.
Make your smile your signature accessory!

These should be in different fonts (clean modern fonts only please- no cursive or busy fonts - Helvetica Neue, Arial and fonts such as those are preferred) and sizes and should be easily legible (minimum font height 4"). Repetitions are ok if needed to fill space.

Font styles to use
Sans Serif

Requirements
Must have
• hese should be in different fonts (clean modern fonts only please- no cursive or busy fonts - Helvetica Neue, Arial and fonts such as those) and sizes and should be easily legible (minimum font height 4"). Repetitions are ok if needed to fill space.
Should not have
• Cursive, busy, fonts.

```html
<!DOCTYPE html>
<html lang="en">
<head>
<meta charset="utf-8">
<title>Smile Quotes Wallpaper</title>
<link href="https://fonts.googleapis.com/css2?family=Baumans&family=Comfortaa:wght@600&family=Montserrat:wght@600&family=Varela+Round&family=Nunito:wght@700&family=Poppins:wght@500&family=Quicksand:wght@600&display=swap" rel="stylesheet">
<style>
  :root {
    --page-bg: #e8edf2;
    --sheet-bg: #ffffff;
    --green: #11944a;
    --lime: #a8c41a;
    --navy: #1d3f7e;
    --blue: #1473bd;
    --magenta: #df1a7b;
    --red: #d5141f;
    --yellow: #f4bc12;
  }
  * { margin: 0; padding: 0; box-sizing: border-box; }
  html, body {
    width: 1200px;
    height: 800px;
    overflow: hidden;
    background: var(--page-bg);
  }
  .wallpaper {
    position: absolute;
    left: 353px;
    top: 20px;
    width: 493px;
    height: 760px;
    background: var(--sheet-bg);
    box-shadow: 0 2px 10px rgba(40, 60, 90, 0.18);
  }
  .quote {
    position: absolute;
    left: 30px;
    right: 30px;
    white-space: nowrap;
  }
  .quote--neglect {
    top: 26px; text-align: left;
    font-family: "Baumans", "Helvetica Neue", sans-serif;
    font-size: 38px; line-height: 44px; color: var(--green);
  }
  .quote--free {
    top: 132px; text-align: right;
    font-family: "Comfortaa", "Helvetica Neue", sans-serif; font-weight: 600;
    font-size: 33px; line-height: 46px; color: var(--lime);
  }
  .quote--floss {
    top: 250px; text-align: center;
    font-family: "Montserrat", Arial, sans-serif; font-weight: 600;
    font-size: 30px; line-height: 40px; color: var(--navy);
  }
  .quote--best {
    top: 312px; text-align: left;
    font-family: "Varela Round", Arial, sans-serif;
    font-size: 46px; line-height: 58px; color: var(--blue);
  }
  .quote--reason {
    top: 452px; text-align: right;
    font-family: "Nunito", Arial, sans-serif; font-weight: 700;
    font-size: 33px; line-height: 40px; color: var(--magenta);
  }
  .quote--world {
    top: 552px; text-align: center;
    font-family: "Poppins", Arial, sans-serif; font-weight: 500;
    font-size: 18px; line-height: 30px; color: var(--red);
  }
  .quote--signature {
    top: 632px; text-align: left;
    font-family: "Quicksand", Arial, sans-serif; font-weight: 600;
    font-size: 36px; line-height: 44px; color: var(--yellow);
  }
</style>
</head>
<body>
  <main class="wallpaper">
    <p class="quote quote--neglect">Dentistry is not<br>Expensive Neglect is!</p>
    <p class="quote quote--free">Smiles are free but<br>they are worth A lot.</p>
    <p class="quote quote--floss">Don’t Forget to Floss!</p>
    <p class="quote quote--best">Put on your best<br>SMILE everyday!</p>
    <p class="quote quote--reason">Be the reason someone<br>smiles today.</p>
    <p class="quote quote--world">Let your SMILE CHANGE THE WORLD,<br>don’t let the world change your smile.</p>
    <p class="quote quote--signature">Make your smile your<br>signature accessory!</p>
  </main>
</body>
</html>
```